2014 Card

I need a vertical business card designed to incorporate 2 Companies in wheaton IL. First company is one o frame (I always type this with no caps and in Cataneo BT font. I like the way the L and the P surround the i) This is a Photography company that does Wedding Photography, Portraiture, Sunset, and many other types of Photography. The website is www.oneoframe-demo.com
The other company is Grand Kiosk Max a Photo Booth rental Company. We rent photo booths to weddings and all types of events. The end project should mainly appeal to Brides and show Class. I have added 2 files One is the Grand Kiosk Max Logo and the other is on one O frames header on the website. I do Like the eye in the sky on the one O frame file

Target Market(s)

Future brides

Industry/Entity Type

Business

Requirements
Must have
• Grand Kiosk Max part should say A Photo Booth Rental Company
one o frame should say All in one photography studio and address should be on this side,

```html
<!DOCTYPE html>
<html lang="en">
<head>
<meta charset="utf-8">
<title>Grand Kiosk Max / one o frame — Business Card</title>
<link rel="stylesheet" href="https://fonts.googleapis.com/css2?family=Source+Sans+3:wght@400;600&display=swap">
<style>
  :root {
    --canvas: #ffffff;
    --front-margin: #f3f3f3;
    --front-card: #ffffff;
    --front-text: #5a5a5a;
    --front-muted: #6f6f6f;
    --brand-text: #4a4a4a;
    --back-base: #000000;
    --back-inner: #0d0d0d;
    --back-text: #ffffff;
    --sky-orange: #d9521c;
    --sky-red: #9a2610;
    --sky-dark: #2a0904;
    --sans: "Source Sans 3", "Myriad Pro", Arial, sans-serif;
  }
  * { margin: 0; padding: 0; box-sizing: border-box; }
  html, body { width: 1200px; height: 1000px; overflow: hidden; background: var(--canvas); }
  body { position: relative; font-family: var(--sans); }

  .card-face { position: absolute; top: 95px; width: 505px; height: 818px; }

  /* Front: Grand Kiosk Max */
  .front { left: 72px; background: var(--front-margin); }
  .front__panel {
    position: absolute; left: 34px; top: 32px; width: 438px; height: 754px;
    background: var(--front-card); overflow: hidden;
  }
  .front__drape {
    position: absolute; inset: 0;
    background: linear-gradient(160deg, #ececec 0%, #ffffff 45%, #f3f3f3 70%, #ffffff 100%);
  }
  .front__contact {
    position: absolute; right: 25px; top: 24px; text-align: right;
    font-size: 20px; line-height: 26px; color: var(--front-muted);
  }
  .front__brand {
    position: absolute; left: 0; right: 0; top: 172px; text-align: center;
    font-size: 48px; font-weight: 600; color: var(--brand-text);
  }
  .front__company { position: absolute; left: 14px; top: 550px; color: var(--front-text); }
  .front__name { font-size: 31px; line-height: 34px; font-weight: 400; }
  .front__tagline { font-size: 14px; line-height: 16px; margin-bottom: 10px; }
  .front__areas { list-style: none; font-size: 20px; line-height: 26px; }

  /* Back: one o frame */
  .back { left: 577px; background: var(--back-base); overflow: hidden; }
  .back__inner {
    position: absolute; left: 33px; top: 32px; width: 440px; height: 754px;
    background: var(--back-inner);
  }
  .back__photo {
    position: absolute; left: 0; top: 0; width: 505px; height: 520px;
    background: linear-gradient(180deg, var(--sky-red) 0%, var(--sky-orange) 35%, var(--sky-orange) 55%, var(--sky-red) 72%, var(--sky-dark) 90%, #000000 100%);
  }
  .back__brand {
    position: absolute; left: 0; right: 0; top: 372px; text-align: center;
    font-size: 56px; line-height: 64px; font-weight: 600; color: #111111;
  }
  .back__studio {
    position: absolute; left: 0; right: 0; top: 444px; text-align: center;
    font-size: 18px; line-height: 22px; color: var(--back-text); letter-spacing: 1px;
  }
  .back__details {
    position: absolute; left: 48px; top: 588px;
    font-size: 20px; line-height: 26px; color: var(--back-text);
  }
  .back__address { font-style: normal; margin-bottom: 10px; }
</style>
</head>
<body>
  <section class="card-face front">
    <div class="front__panel">
      <div class="front__drape" role="img" aria-label="Soft white silk drape background"></div>
      <div class="front__contact">
        <p>Tel: 630-555-0142</p>
        <p>Email: hello@grandkioskmax-demo.com</p>
      </div>
      <p class="front__brand">Grand Kiosk Max</p>
      <div class="front__company">
        <h2 class="front__name">Grand Kiosk Max</h2>
        <p class="front__tagline">a Photo Booth rental Company</p>
        <ul class="front__areas">
          <li>Chicago Area</li>
          <li>Los Angeles Area</li>
          <li>Phoenix Area</li>
          <li>Springfield, IL. Area</li>
        </ul>
      </div>
    </div>
  </section>

  <section class="card-face back">
    <div class="back__inner"></div>
    <div class="back__photo" role="img" aria-label="Photograph of the sun setting through red and orange clouds"></div>
    <p class="back__brand">one o frame</p>
    <p class="back__studio">All in one photography studio</p>
    <div class="back__details">
      <address class="back__address">
        one o frame<br>
        418 N Linden Ave.<br>
        Wheaton IL 60187
      </address>
      <p>Tel: 630-555-0142</p>
      <p>Email: hello@grandkioskmax-demo.com</p>
      <p>Follow @oneoframe on Chirper</p>
    </div>
  </section>
</body>
</html>
```